Support People to improve their image and well-being by provided personalised advise

We need a design for business cards that could be used for production on plato press. We build a new business in our region for advising mostly women (also men though) on style embracing several aspects including fashion, style, self-confidence and ultimately your internal and external image. The business card should be "classy", "french-style". The business is located in the french -speaking part of Switzerland, close to France. The name of the company is Velo Grace

Target Market(s)

Service fees won't be cheap (medium to premium) thus we target mid-class to upper-class women (1st target) and men (2nd target)

Industry/Entity Type

Life Coaching

Contact Information for Business Card

Conseil en Image

+41 79 418 62 07
morinetu@velo-grace.ch
linkedin.com/in/tu-moro-netia

Logo Text

Velo Grace

Colors

Designer to choose colors to be used in the design.

```html
<!DOCTYPE html>
<html lang="en">
<head>
<meta charset="utf-8">
<title>Velo Grace — Business Cards</title>
<link rel="stylesheet" href="https://fonts.googleapis.com/css2?family=Cormorant+Garamond:ital,wght@0,500&family=Courier+Prime&display=swap">
<style>
  :root {
    --backdrop: #6a5848;
    --card: #efe8da;
    --card-edge: #e4dac6;
    --ink: #2a2420;
    --ink-soft: #8f8072;
    --accent: #8a7262;
    --serif: "Cormorant Garamond", Georgia, serif;
    --mono: "Courier Prime", "Courier New", monospace;
  }
  * { margin: 0; padding: 0; box-sizing: border-box; }
  html, body {
    width: 900px;
    height: 1200px;
    overflow: hidden;
    background: var(--backdrop);
  }
  .canvas {
    position: relative;
    width: 900px;
    height: 1200px;
  }
  .card {
    position: absolute;
    left: 88px;
    width: 732px;
    height: 428px;
    border-radius: 24px;
    background: radial-gradient(ellipse at 40% 35%, #f3eee3 0%, var(--card) 55%, var(--card-edge) 100%);
    box-shadow: 0 6px 14px rgba(0, 0, 0, 0.35);
  }
  .card--front { top: 137px; }
  .card--back { top: 634px; }

  .wordmark {
    position: absolute;
    left: 0;
    width: 100%;
    text-align: center;
  }
  .wordmark__name {
    display: inline-block;
    font-family: var(--serif);
    font-weight: 500;
    font-size: 64px;
    line-height: 1;
    color: var(--ink);
    letter-spacing: 1px;
    padding-left: 90px;
  }
  .wordmark__tag {
    position: absolute;
    right: 148px;
    top: 72px;
    font-family: var(--mono);
    font-size: 15px;
    letter-spacing: 1px;
    color: var(--accent);
  }
  .card--front .wordmark { top: 112px; }
  .card--back .wordmark { top: 140px; }

  .details {
    position: absolute;
    left: 0;
    top: 244px;
    width: 100%;
    text-align: center;
  }
  .details__name {
    font-family: var(--serif);
    font-weight: 500;
    font-size: 38px;
    line-height: 1;
    color: var(--ink);
  }
  .details__role {
    margin-top: 12px;
    font-family: var(--serif);
    font-size: 16px;
    color: var(--ink-soft);
  }
  .details__rule {
    width: 10px;
    height: 1.5px;
    margin: 10px auto 12px;
    background: var(--ink);
  }
  .details__contact,
  .details__web {
    font-family: var(--mono);
    font-size: 15px;
    letter-spacing: 0.6px;
    color: var(--ink);
  }
  .details__web { margin-top: 9px; }
</style>
</head>
<body>
<main class="canvas">
  <section class="card card--front">
    <div class="wordmark">
      <span class="wordmark__name">Velo Grace</span>
      <span class="wordmark__tag">French</span>
    </div>
    <div class="details">
      <p class="details__name">Lina Moreau</p>
      <p class="details__role">Style Advisor</p>
      <div class="details__rule"></div>
      <p class="details__contact">P: 0917-2260-4813 • E: info@velograce.com</p>
      <p class="details__web">www.VeloGrace.com</p>
    </div>
  </section>

  <section class="card card--back">
    <div class="wordmark">
      <span class="wordmark__name">Velo Grace</span>
      <span class="wordmark__tag">French</span>
    </div>
  </section>
</main>
</body>
</html>
```